Heaven, guard me from choosing Korith

I need a book cover to be designed for a book I am writing about marrying the wrong man. I need the cover to be very eye-catching with an emotional, sympathetic and compassionate feel. Gold can be used along with any other colours . I want a very feminine feel to the book cover. I don't mind a cartoon design but must be elegant,
Let me give you a hint about Korith, he is a very wealthy man, good looking a narcissist, a high flyer jet-setter, very very mean with his money. Really know how to pull the girls but treat them badly, he is the kind of man any women would fall for. With this information create me a cover that when any women look at they can identify and will buy the book.
Target Market(s)
Female, single women, divorced women, women who are dating.
Colors
Designer to choose colors to be used in the design.
Requirements
Must have
- must have some kind of picture o to it, bold writing of the book title yet soft in appearance. Elegant, sophisticated and very expensive yet attractive. Modern in appearance very much 21st century look to it. please stay away from the church, wedding dress.
Nice to have
- Nice to have a playful cover, yet very elegant and modern.
Should not have
- The design of the book cover should not have, any church wedding dress graphics. The book size is a jpg at 300 dpi with A5 dimensions (14.8 cm wide by 21 cm high), and make sure that your text is well within the trim line - approximately 2 cm from the edge.
- This is my autobiography
- This book aims to teach you informative Guide and strategies, how to attract the right kind of man to be your husband. What you also learn is how to understand the social fundamental truth sharps the relationship the man will have with himself and the rest of the world.
- This book will uncover the 10 worst men to Marry, using the biblical character to name these bad boys, you will learn that in today's 21st century these character is still very much around.
- Things you will learn from reading this book.
- .Break the cycle of the failed relationship.
- .Understanding the fundamental truth about a man life.
- . Recognize red flags you should not ignore when dating.
- .Strategies on how to win the spiritual on singleness
- . The do's and don't of dating.
- .How to equip yourself to defeat the curse anti-marriage
- Dovella Brannick is co-leader with her husband Marcus Brannick Beacon 700 prayer ministry in London, England where they live with their three grown children and Ethan their energetic 13yrs old superstar. The ministry is renowned for their Deliverance services and Teaching where Dovella teaches the word of God with deep spiritual insight. She also has a prophetic insight into dreams and vision from a biblical perspective. Beacon 700 prayer ministry is a 24 hours prayer warriors group who observe the 8 prayer watches. The ministry is known for their powerful teaching seminar as well there 72 prayer hours shut-in service,as well as their mentorship programme and master classes on singleness and marriages.
- please put the picture of my self on the back. I have uploaded

```html
<!DOCTYPE html>
<html lang="en">
<head>
<meta charset="utf-8">
<title>Heaven, guard me from choosing Korith — Book Cover</title>
<link rel="stylesheet" href="https://fonts.googleapis.com/css2?family=Sacramento&family=Oswald:wght@300&display=swap">
<style>
  :root {
    --paper: #ece8df;
    --ink: #141414;
    --gold: #c9a14a;
    --gold-bright: #d9ad45;
    --gold-deep: #a9771f;
  }
  html, body {
    margin: 0;
    padding: 0;
    width: 846px;
    height: 1200px;
    overflow: hidden;
    background: var(--paper);
  }
  .cover {
    position: relative;
    width: 846px;
    height: 1200px;
    background: var(--paper);
    overflow: hidden;
  }
  .frame {
    position: absolute;
    inset: 0;
  }
  .foliage {
    position: absolute;
  }
  .foliage--top {
    right: 0;
    top: 0;
    width: 425px;
    height: 190px;
  }
  .foliage--bottom {
    left: 0;
    bottom: 0;
    width: 425px;
    height: 185px;
  }
  .title {
    position: absolute;
    left: 0;
    right: 0;
    top: 392px;
    margin: 0;
    text-align: center;
    font-family: "Sacramento", cursive;
    font-weight: 400;
    font-size: 104px;
    line-height: 98px;
    color: var(--ink);
  }
  .title span {
    display: block;
  }
  .subtitle {
    position: absolute;
    right: 132px;
    top: 700px;
    margin: 0;
    font-family: "Oswald", sans-serif;
    font-weight: 300;
    font-size: 22px;
    letter-spacing: 5px;
    color: var(--ink);
  }
  .dedication {
    position: absolute;
    right: 108px;
    top: 1060px;
    margin: 0;
    font-family: "Oswald", sans-serif;
    font-weight: 300;
    font-size: 36px;
    letter-spacing: 5px;
    color: var(--ink);
  }
</style>
</head>
<body>
<main class="cover">
  <svg class="frame" width="846" height="1200" viewBox="0 0 846 1200" aria-hidden="true">
    <rect x="62" y="64" width="720" height="1072" fill="none" stroke="var(--ink)" stroke-width="2"/>
    <rect x="69" y="71" width="707" height="1058" fill="none" stroke="var(--gold)" stroke-width="2"/>
  </svg>

  <svg class="foliage foliage--top" viewBox="0 0 425 190" role="img" aria-label="Gold leafy branch with berries sweeping across the top right corner">
    <defs>
      <radialGradient id="leafGlowTop" cx="62%" cy="38%" r="62%">
        <stop offset="0" stop-color="var(--gold-bright)" stop-opacity="1"/>
        <stop offset="0.55" stop-color="var(--gold)" stop-opacity="0.85"/>
        <stop offset="1" stop-color="var(--gold-deep)" stop-opacity="0"/>
      </radialGradient>
    </defs>
    <rect width="425" height="190" fill="url(#leafGlowTop)"/>
  </svg>

  <svg class="foliage foliage--bottom" viewBox="0 0 425 185" role="img" aria-label="Gold leafy branch with berries rising from the bottom left corner">
    <defs>
      <radialGradient id="leafGlowBottom" cx="40%" cy="65%" r="62%">
        <stop offset="0" stop-color="var(--gold-bright)" stop-opacity="1"/>
        <stop offset="0.55" stop-color="var(--gold)" stop-opacity="0.85"/>
        <stop offset="1" stop-color="var(--gold-deep)" stop-opacity="0"/>
      </radialGradient>
    </defs>
    <rect width="425" height="185" fill="url(#leafGlowBottom)"/>
  </svg>

  <h1 class="title">
    <span>Heaven, guard me</span>
    <span>from</span>
    <span>choosing Korith</span>
  </h1>
  <p class="subtitle">WITH DO'S AND DON'TS.</p>
  <p class="dedication">FOR DOVELLA.</p>
</main>
</body>
</html>
```